Flyer in Creole

Instructions for Designer
Objective: Create two versions of the flyer for Densora dental services: one in French and one in Creole. Target audience is elders of the haitian community in Montreal so include picture of an older person with a darker skin complexion.

I have included our original flyer.

Densora - Sèvis Dantè pou Granmoun Aje
Nou ofri swen dantè san frè pou moun 65 an e plis!

La Clinique Dentaire Densora gen kè kontan patisipe nan Pwogram Sourir Nasyonal (PSNB). Si w gen 65 an oubyen plis, ou ka resevwa swen dantè gratis, san frè siplemantè si w kalifye.

Kijan pou Kalifye?

Si w gen 65 an ou plis, ou ka jwenn tretman dantè san frè.
Vizite: https://www.plansourir-exemple.org/aplike/fomile.html pou w aplike epi w konnen si w kalifye.
Sèvis Nou Ofri:

Netwayaj dantè: Sante bouch ou enpòtan, fè yon netwayaj pwofesyonèl pou prezève sante dantè w.
Egzamen ak radyografi: Pran yon randevou pou yon egzamen konplè ak radyografi.
Ekstraksyon dantè: Retire dan ki domaje oswa ki fè w mal.
Ijans dantè: Tretman rapid pou doulè, dan kase, oswa lòt ijans.
Pwotèz dantè konplè ak pasyèl: Nou ranplase dan ki manke yo pou yon bèl souri ak bon sante.
Rele Kounye a pou Fiks yon Randevou: 514-555-0187
Klinik Densora - 2860 Rue Belmarais E, 2yèm etaj, Montreal, QC H2X 3K9
Design Elements:
Use images that resonate with the Creole-speaking community.
Ensure the text is clear and accessible.

```html
<!DOCTYPE html>
<html lang="ht">
<head>
<meta charset="utf-8">
<title>Densora – Sèvis Dantè pou Granmoun Aje</title>
<link rel="stylesheet" href="https://fonts.googleapis.com/css2?family=Fraunces:opsz,wght@9..144,500;9..144,600;9..144,700&family=Source+Serif+4:opsz,wght@8..60,400;8..60,600;8..60,700&display=swap">
<style>
  :root{
    --navy:#1e2d47;
    --navy-deep:#16223a;
    --sky:#a9c8f0;
    --ink:#1f2c45;
    --paper:#ffffff;
    --backdrop:#232323;
    --leaf-dark:#2f3d1f;
    --leaf-light:#5d6a34;
  }
  *{margin:0;padding:0;box-sizing:border-box}
  html,body{width:1200px;height:1200px;overflow:hidden;background:var(--backdrop)}
  .canvas{position:relative;width:1200px;height:1200px}
  .flyer{
    position:absolute;left:167px;top:40px;width:1310px;height:1695px;
    transform:scale(0.661);transform-origin:0 0;background:var(--paper);overflow:hidden;
    font-family:"Source Serif 4",Georgia,serif;color:var(--ink);
  }
  .flyer-shapes{position:absolute;inset:0}
  .abs{position:absolute}
  .headline{
    left:44px;top:452px;font-family:"Fraunces",Georgia,serif;font-weight:700;
    font-size:74px;line-height:77px;color:var(--sky);letter-spacing:0.5px;
  }
  .tagline{left:44px;top:766px;font-size:39px;line-height:43px;color:#fff}
  .tagline strong{color:var(--sky);font-weight:700}
  .intro{left:602px;top:676px;width:665px;font-size:27px;line-height:34px;text-align:justify}
  .intro strong{font-family:"Fraunces",Georgia,serif;font-weight:600}
  .qualify{left:455px;top:850px;width:855px;height:195px;background:var(--sky);border-radius:34px 0 0 34px}
  .qualify-frame{position:absolute;left:10px;top:10px;right:-4px;bottom:10px;border:2px dashed var(--ink);border-right:none;border-radius:28px 0 0 28px}
  .qualify h2{position:absolute;left:52px;top:22px;font-family:"Fraunces",Georgia,serif;font-weight:600;font-size:34px}
  .qualify p{position:absolute;left:52px;top:70px;width:770px;font-size:24px;line-height:36px}
  .qualify .link{font-weight:700;word-break:break-all}
  .services-title{left:512px;top:1068px;font-family:"Fraunces",Georgia,serif;font-weight:600;font-size:35px}
  .service{left:505px;width:770px}
  .service-icon{position:absolute;left:0;top:4px;width:76px;height:76px}
  .service h3{margin-left:93px;font-family:"Fraunces",Georgia,serif;font-weight:600;font-size:29px;line-height:34px}
  .service p{margin-left:93px;font-size:25px;line-height:30px;text-align:justify}
  .rule{left:515px;width:757px;border-top:2px dashed var(--ink)}
  .brand{left:42px;top:1250px;width:390px;font-family:"Fraunces",Georgia,serif;font-weight:600;font-size:98px;line-height:110px;color:var(--ink);letter-spacing:-1px;white-space:nowrap}
  .brand-rule{left:44px;top:1387px;width:386px;border-top:2px dotted var(--ink)}
  .call{left:44px;top:1396px;font-size:41px;line-height:48px}
  .phone{left:42px;top:1496px;font-family:"Fraunces",Georgia,serif;font-weight:700;font-size:60px;letter-spacing:-2px;white-space:nowrap}
  .address{left:44px;top:1590px;font-size:25px;line-height:35px}
  .footer-band{left:0;top:1672px;width:1310px;height:23px;background:var(--navy)}
</style>
</head>
<body>
<div class="canvas">
  <div class="flyer">
    <svg class="flyer-shapes" viewBox="0 0 1310 1695" width="1310" height="1695">
      <defs>
        <radialGradient id="leafGlow" cx="0.6" cy="0.3" r="0.8">
          <stop offset="0" stop-color="var(--leaf-light)"/>
          <stop offset="1" stop-color="var(--leaf-dark)"/>
        </radialGradient>
        <linearGradient id="navyFade" x1="0" y1="0" x2="1" y2="1">
          <stop offset="0" stop-color="var(--navy)"/>
          <stop offset="1" stop-color="var(--navy-deep)"/>
        </linearGradient>
      </defs>
      <path role="img" aria-label="Foto yon granmoun fanm ki ap souri devan pyebwa vèt"
            d="M0,0 L1310,0 L1310,472 C1180,590 1010,656 880,654 C780,650 700,620 644,572 Z" fill="url(#leafGlow)"/>
      <path role="img" aria-label="Foto yon pasyan k ap resevwa swen dantè, ak koulè ble fonse"
            d="M0,130 Q0,105 30,108 Q60,110 95,140 L545,535 Q610,600 548,672 L135,1175 Q95,1220 40,1220 Q0,1218 0,1190 Z" fill="url(#navyFade)"/>
    </svg>

    <h1 class="abs headline">SÈVIS<br>DANTÈ POU<br>GRANMOUN<br>AJE</h1>
    <p class="abs tagline">Nou ofri swen<br>dantè san frè pou<br><strong>moun 65 an e plis!</strong></p>

    <p class="abs intro">La Clinique Dentaire Densora gen kè kontan patisipe nan <strong>Pwogram Sourir Nasyonal (PSNB).</strong> Si w gen 65 an oubyen plis, ou ka resevwa swen dantè gratis, san frè siplemantè si w kalifye.</p>

    <section class="abs qualify">
      <div class="qualify-frame"></div>
      <h2>Kijan pou Kalifye?</h2>
      <p>Si w gen 65 an ou plis, ou ka jwenn tretman dantè san frè. Vizite: <span class="link">https://www.plansourir-exemple.org/aplike/fomile.html</span> pou w aplike epi w konnen si w kalifye.</p>
    </section>

    <h2 class="abs services-title">Sèvis Nou Ofri:</h2>

    <div class="abs service" style="top:1130px">
      <svg class="service-icon" viewBox="0 0 76 76"><circle cx="38" cy="38" r="36" fill="none" stroke="var(--ink)" stroke-width="1.5" stroke-dasharray="4 3"/><circle cx="38" cy="38" r="31" fill="var(--navy)"/><path d="M27 30c0-6 6-7 11-4 5-3 11-2 11 4 0 6-3 8-4 16-1 5-4 5-5 0l-2-7-2 7c-1 5-4 5-5 0-1-8-4-10-4-16z" fill="var(--sky)"/></svg>
      <h3>Netwayaj dantè:</h3>
      <p>Sante bouch ou enpòtan, fè yon netwayaj pwofesyonèl pou prezève sante dantè w.</p>
    </div>
    <div class="abs rule" style="top:1232px"></div>

    <div class="abs service" style="top:1243px">
      <svg class="service-icon" viewBox="0 0 76 76"><circle cx="38" cy="38" r="36" fill="none" stroke="var(--ink)" stroke-width="1.5" stroke-dasharray="4 3"/><circle cx="38" cy="38" r="31" fill="var(--navy)"/><path d="M26 28c0-7 7-8 12-5 5-3 12-2 12 5 0 7-3 9-4 18-1 6-5 6-6 0l-2-8-2 8c-1 6-5 6-6 0-1-9-4-11-4-18z" fill="none" stroke="var(--sky)" stroke-width="3"/><circle cx="38" cy="36" r="4" fill="var(--sky)"/></svg>
      <h3>Egzamen ak radyografi:</h3>
      <p>Pran yon randevou pou yon egzamen konplè ak radyografi.</p>
    </div>
    <div class="abs rule" style="top:1347px"></div>

    <div class="abs service" style="top:1362px">
      <svg class="service-icon" viewBox="0 0 76 76"><circle cx="38" cy="38" r="36" fill="none" stroke="var(--ink)" stroke-width="1.5" stroke-dasharray="4 3"/><circle cx="38" cy="38" r="31" fill="var(--navy)"/><path d="M28 18l8 14M48 18l-8 14" stroke="var(--sky)" stroke-width="4" stroke-linecap="round"/><path d="M28 40c0-5 5-6 10-3 5-3 10-2 10 3 0 5-2 7-3 13-1 4-4 4-5 0l-2-5-2 5c-1 4-4 4-5 0-1-6-3-8-3-13z" fill="var(--sky)"/></svg>
      <h3>Ekstraksyon dantè:</h3>
      <p>Retire dan ki domaje oswa ki fè w mal.</p>
    </div>
    <div class="abs rule" style="top:1442px"></div>

    <div class="abs service" style="top:1458px">
      <svg class="service-icon" viewBox="0 0 76 76"><circle cx="38" cy="38" r="36" fill="none" stroke="var(--ink)" stroke-width="1.5" stroke-dasharray="4 3"/><circle cx="38" cy="38" r="31" fill="var(--navy)"/><path d="M30 30c0-6 6-7 11-4 5-3 11-2 11 4 0 6-3 8-4 16-1 5-4 5-5 0l-2-7-2 7c-1 5-4 5-5 0-1-8-4-10-4-16z" fill="var(--sky)"/><circle cx="28" cy="28" r="8" fill="var(--navy)" stroke="var(--sky)" stroke-width="2"/><path d="M28 24v8M24 28h8" stroke="var(--sky)" stroke-width="2"/></svg>
      <h3>Ijans dantè:</h3>
      <p>Tretman rapid pou doulè, dan kase, oswa lòt ijans.</p>
    </div>
    <div class="abs rule" style="top:1545px"></div>

    <div class="abs service" style="top:1556px">
      <svg class="service-icon" viewBox="0 0 76 76"><circle cx="38" cy="38" r="36" fill="none" stroke="var(--ink)" stroke-width="1.5" stroke-dasharray="4 3"/><circle cx="38" cy="38" r="31" fill="var(--navy)"/><path d="M20 50c0-18 8-26 18-26s18 8 18 26" fill="none" stroke="var(--sky)" stroke-width="6" stroke-dasharray="5 2"/><path d="M28 50c0-12 4-18 10-18s10 6 10 18" fill="none" stroke="var(--sky)" stroke-width="2"/></svg>
      <h3>Pwotèz dantè konplè ak pasyèl:</h3>
      <p>Nou ranplase dan ki manke yo pou yon bèl souri ak bon sante.</p>
    </div>

    <div class="abs brand">densora</div>
    <div class="abs brand-rule"></div>
    <p class="abs call">Rele Kounye a pou<br>Fiks yon Randevou:</p>
    <p class="abs phone">514-555-0187</p>
    <p class="abs address">2860 Rue Belmarais E, 2Yèm Etaj,<br>Montreal, QC H2X 3K9</p>

    <div class="abs footer-band"></div>
  </div>
</div>
</body>
</html>
```